Dorsey K. Wendell Business Card

We need a business card for our company Dorsey K. Wendell Heating & Plumbing to be distributed to potential customers. It should follow the color scheme of our logo and have a modern upscale and masculine look.

The logo is attached and the info below should also be included:

5187 W. Cedar Brook Rd.
Ashbury, PA 17390

Russell T. Wendell
(717) 592-0817
russelltwendell@fernmail.net
dorseykwendell.net
PA #093148

Industry/Entity Type

Business

Contact Information for Business Card

5187 W. Cedar Brook Rd.
Ashbury, PA 17390

Russell T. Wendell
(717) 592-0817
russelltwendell@fernmail.net
dorseykwendell.net
PA #093148

Colors

Designer to choose colors to be used in the design.

Requirements
Must have
• Information above included

```html
<!DOCTYPE html>
<html lang="en">
<head>
<meta charset="utf-8">
<title>Dorsey K. Wendell Business Card</title>
<link rel="stylesheet" href="https://fonts.googleapis.com/css2?family=Lato:wght@400;700;900&display=swap">
<style>
  :root {
    --brand-blue: #0a56a8;
    --brand-blue-dark: #07468c;
    --brand-green: #8cc63f;
    --ink: #2b2b2b;
    --paper: #ffffff;
    --backdrop: #e9e6e1;
  }
  * { box-sizing: border-box; margin: 0; padding: 0; }
  html, body { width: 1200px; height: 900px; overflow: hidden; }
  body {
    background: var(--backdrop);
    font-family: "Lato", sans-serif;
    display: flex;
    flex-direction: column;
    align-items: center;
    justify-content: center;
    gap: 36px;
  }
  .card {
    width: 700px;
    height: 400px;
    position: relative;
    box-shadow: 0 10px 30px rgba(0,0,0,0.18);
    overflow: hidden;
  }
  .card-back {
    background: linear-gradient(135deg, var(--brand-blue) 0%, var(--brand-blue-dark) 100%);
    display: flex;
    align-items: center;
    justify-content: center;
  }
  .wordmark {
    display: flex;
    align-items: center;
    gap: 14px;
    font-weight: 900;
    letter-spacing: 0.04em;
    text-transform: uppercase;
    white-space: nowrap;
  }
  .wordmark-square { width: 34px; height: 34px; flex: none; }
  .card-back .wordmark { color: var(--paper); font-size: 34px; }
  .card-back .wordmark-square { background: var(--paper); }
  .card-front { background: var(--paper); }
  .contact {
    position: absolute;
    left: 56px;
    top: 64px;
    color: var(--ink);
    font-size: 15px;
    line-height: 1.55;
  }
  .contact-name {
    color: var(--brand-blue);
    font-size: 25px;
    font-weight: 400;
    margin-bottom: 18px;
  }
  .contact-line { display: flex; align-items: center; gap: 10px; }
  .contact-line svg { width: 13px; height: 13px; fill: var(--brand-blue); flex: none; }
  .contact-address { margin-top: 12px; }
  .card-front .wordmark {
    position: absolute;
    right: 56px;
    top: 150px;
    color: var(--brand-blue);
    font-size: 24px;
  }
  .card-front .wordmark-square { width: 28px; height: 28px; background: var(--brand-blue); }
  .license {
    position: absolute;
    right: 60px;
    bottom: 46px;
    font-size: 15px;
    color: var(--ink);
    display: flex;
    align-items: center;
    gap: 10px;
  }
  .license::before {
    content: "";
    width: 4px;
    height: 18px;
    background: var(--brand-green);
  }
  .edge-band {
    position: absolute;
    left: 0; right: 0; bottom: 0;
    height: 14px;
    background: linear-gradient(90deg, var(--brand-blue) 0%, var(--brand-blue) 45%, rgba(10,86,168,0) 100%);
  }
</style>
</head>
<body>
  <section class="card card-back">
    <div class="wordmark"><span class="wordmark-square"></span>Dorsey K. Wendell</div>
  </section>

  <section class="card card-front">
    <div class="contact">
      <h1 class="contact-name">Russell T. Wendell</h1>
      <p class="contact-line">
        <svg viewBox="0 0 16 16" aria-hidden="true"><path d="M3.6 1.2l2.3 2.6-1.4 1.8c.9 2 2.5 3.6 4.5 4.6l1.8-1.4 2.6 2.3-1.3 2.6C6.9 13.5 2.5 9.1 1 3.9z"/></svg>
        (717) 592-0817
      </p>
      <p class="contact-line">
        <svg viewBox="0 0 16 16" aria-hidden="true"><path d="M1 3h14v10H1z M1.8 3.8L8 8.6l6.2-4.8" fill="none" stroke="#0a56a8" stroke-width="1.6"/></svg>
        russelltwendell@fernmail.net
      </p>
      <p class="contact-line">
        <svg viewBox="0 0 16 16" aria-hidden="true"><circle cx="8" cy="8" r="6.5" fill="none" stroke="#0a56a8" stroke-width="1.5"/><path d="M1.5 8h13M8 1.5c-3 3.5-3 9.5 0 13M8 1.5c3 3.5 3 9.5 0 13" fill="none" stroke="#0a56a8" stroke-width="1.2"/></svg>
        www.dorseykwendell.net
      </p>
      <p class="contact-address">5187 W. Cedar Brook Rd.<br>Ashbury, PA 17390</p>
    </div>

    <div class="wordmark"><span class="wordmark-square"></span>Dorsey K. Wendell</div>

    <p class="license">PA #093148</p>
    <div class="edge-band"></div>
  </section>
</body>
</html>
```